We need a small, simple graphic for the company newsletter. The topic of this issue is voting. As a company, we believe it is important to vote; therefore, we're going to explain the importance of voting, how to vote, when to vote, and how the company will be providing time off to vote. We would like the graphic to be simple (2-3 colors) and look like the sticker or pin you received after voting that says "I voted". We would like our company logo incorporated somehow, so be creative. It must contain our company color of blue (r 38, g 58, b 128). The company logo is attached, as well as some I voted stickers for reference

Requirements
Must have
• Use our company color of blue (r 38 g 58 b 128). Use the words "I Voted". Use the company font Bebas and/or Helvetica Neue. The background must be white as it will be incorporated into a newsletter document.
Nice to have
• Incorporate the company logo. American flag
Should not have
• fireworks, reference to 2020

```html
<!DOCTYPE html>
<html lang="en">
<head>
<meta charset="utf-8">
<title>I Voted Sticker</title>
<link href="https://fonts.googleapis.com/css2?family=Roboto+Condensed:wght@400;700&display=swap" rel="stylesheet">
<style>
  :root {
    --page-white: #ffffff;
    --company-blue: #263a80;
    --sticker-ink: #ececec;
    --flag-red: #c8383f;
    --flag-light: #f1eeee;
    --flag-navy: #2f4a92;
  }
  html, body {
    margin: 0;
    padding: 0;
    width: 1200px;
    height: 1000px;
    overflow: hidden;
    background: var(--page-white);
  }
  .canvas {
    display: block;
    width: 1200px;
    height: 1000px;
  }
  .sticker-base { fill: var(--company-blue); }
  .headline {
    font-family: "Roboto Condensed", "Helvetica Neue", Arial, sans-serif;
    font-weight: 700;
    font-size: 190px;
    fill: var(--sticker-ink);
  }
  .brand-name {
    font-family: "Roboto Condensed", "Helvetica Neue", Arial, sans-serif;
    font-weight: 700;
    font-size: 38px;
    fill: var(--sticker-ink);
    letter-spacing: 2px;
  }
  .brand-mark { fill: var(--sticker-ink); }
</style>
</head>
<body>
<svg class="canvas" viewBox="0 0 1200 1000" xmlns="http://www.w3.org/2000/svg">
  <defs>
    <clipPath id="sticker-shape">
      <circle cx="600" cy="490" r="265"/>
    </clipPath>
    <linearGradient id="flag-tones" x1="0" y1="0" x2="1" y2="0">
      <stop offset="0" stop-color="var(--flag-navy)"/>
      <stop offset="0.3" stop-color="var(--flag-navy)"/>
      <stop offset="0.5" stop-color="var(--flag-red)"/>
      <stop offset="0.8" stop-color="var(--flag-red)"/>
      <stop offset="1" stop-color="var(--flag-light)"/>
    </linearGradient>
  </defs>

  <g class="sticker" clip-path="url(#sticker-shape)">
    <circle class="sticker-base" cx="600" cy="490" r="265"/>
    <path class="flag-area" role="img" aria-label="Waving American flag"
          fill="url(#flag-tones)"
          d="M 440 200 L 880 200 L 880 470
             C 840 455, 800 470, 760 478
             C 720 486, 680 462, 630 452
             C 580 442, 520 448, 440 456 Z"/>
    <text class="headline" x="605" y="610" text-anchor="middle" textLength="390" lengthAdjust="spacingAndGlyphs">I VOTED</text>
    <g class="brand">
      <rect class="brand-mark" x="508" y="666" width="14" height="14"/>
      <text class="brand-name" x="532" y="688">HALVERSON</text>
    </g>
  </g>
</svg>
</body>
</html>
```